New Menu for Elegant Cafe Pastry Shop

We need to choose a design and layout for our new menu. We would like to also condense our current menu to 4-6 pages.
We will be changing prices and items on the menu, so it needs to be editable. Adobe formats are preferred. The size of the pages needs to be letter size. We will be printing it in house
Please take inspiration from the photos of our shop and food and also our Picmosaic page.
Attached are our current menu our logo and the logo info

https://www.picmosaic.com/marbrecoquette/?hl=en
https://maps.wayfindr.app/Qk3Lm9Xp2Tb7VwR4a

Industry/Entity Type

Food Cafe Bakery pastry

Other font styles liked:
• please look at attached files

Colors

Designer to choose colors to be used in the design.

Requirements
Nice to have
• Use of Arches like on our shop wallpaper or oblong eclair shapes, Art Deco elements

```html
<!DOCTYPE html>
<html lang="en">
<head>
<meta charset="utf-8">
<title>Marbre Coquette – Menu</title>
<link href="https://fonts.googleapis.com/css2?family=Josefin+Sans:wght@300;400;600;700&display=swap" rel="stylesheet">
<style>
:root{
  --sky:#c4ebf9;
  --paper:#fdf1f5;
  --blush:#fbe3ec;
  --rose:#f3a9bf;
  --leaf:#9cc4a0;
  --gold:#d9b870;
  --teal:#3bb5bf;
  --plum:#3d2a2f;
  --muted:#6d5a5f;
  --line:#b8a6ab;
  --tag:#f6b6cb;
}
*{box-sizing:border-box;margin:0;padding:0}
html,body{width:1200px;height:600px;overflow:hidden}
body{background:var(--sky);font-family:"Josefin Sans",sans-serif;color:var(--plum)}
.page{position:absolute;top:62px;width:368px;height:475px;background:var(--blush);overflow:hidden}
.florals{position:absolute;inset:0;
  background:
   radial-gradient(circle at 6% 4%,var(--rose) 0,transparent 16%),
   radial-gradient(circle at 94% 4%,var(--rose) 0,transparent 16%),
   radial-gradient(circle at 6% 97%,var(--rose) 0,transparent 16%),
   radial-gradient(circle at 94% 97%,var(--rose) 0,transparent 16%),
   radial-gradient(circle at 3% 50%,var(--leaf) 0,transparent 8%),
   radial-gradient(circle at 97% 50%,var(--leaf) 0,transparent 8%),
   linear-gradient(#f7cbd8,#fbe3ec 50%,#f7cbd8)}
.sheet{position:absolute;left:18px;right:18px;top:14px;bottom:14px;background:linear-gradient(#fdf3f6,var(--paper));border:1px solid var(--gold);box-shadow:inset 0 0 0 2px var(--paper),inset 0 0 0 2.6px var(--gold)}
.at{position:absolute}
.h{font-weight:300;text-transform:uppercase;letter-spacing:.05em;font-size:10px;color:var(--plum);white-space:nowrap}
.title{font-weight:300;text-transform:uppercase;letter-spacing:.04em;font-size:13.5px;color:var(--teal);text-align:center;white-space:nowrap}
.sub{font-size:5px;font-weight:700;letter-spacing:.28em;text-align:center;text-transform:uppercase}
.rule{position:absolute;height:2.4px;border-top:.6px solid var(--line);border-bottom:.6px solid var(--line)}
.vr{position:absolute;width:0;border-left:.6px solid var(--line)}
.row{display:flex;align-items:baseline;font-size:5px;font-weight:700;text-transform:uppercase;height:12px;line-height:12px;white-space:nowrap}
.tight .row{height:10.5px;line-height:10.5px;font-size:4.4px}
.row .lead{flex:1;border-bottom:.4px solid var(--line);margin:0 3px;transform:translateY(-1.5px)}
.desc{font-size:4.2px;line-height:6px;color:var(--muted);font-weight:400}
.mark{display:inline-block;width:4px;height:4px;border-radius:50%;background:#a07a4b;margin-left:3px;transform:translateY(-.5px)}
.mark.gf{background:#d2a36b;border-radius:1px}
.mark.vg{background:#9ccc7a}
.tag{display:inline-block;font-size:3.4px;font-weight:600;color:#fff;background:var(--tag);padding:1px 4px;margin-left:4px;letter-spacing:.05em;vertical-align:middle}
.logo-dot{width:22px;height:22px;border-radius:50%;background:var(--teal)}
.brand{font-size:9.5px;font-weight:400;letter-spacing:.06em;color:var(--plum);white-space:nowrap}
.address{font-size:7px;line-height:9px;letter-spacing:.04em;text-transform:uppercase}
.address .tel{color:var(--teal)}
.address svg{width:6px;height:6px;vertical-align:-.5px;fill:var(--teal)}
.legend{display:flex;gap:9px;font-size:4px;font-weight:600;text-transform:uppercase;white-space:nowrap;align-items:center}
.legend span{display:flex;align-items:center;gap:2px}
.legend i{display:inline-block;width:5px;height:5px;border-radius:50%}
.sides{border:.6px solid var(--line);outline:.6px solid var(--line);outline-offset:-2.5px}
.note{font-size:4.4px;font-weight:700;text-align:center;line-height:6.5px;text-transform:uppercase}
.extras{font-size:4.2px;font-weight:700;text-align:center;line-height:8px;text-transform:uppercase;white-space:nowrap}
</style>
</head>
<body>

<!-- Page 1: seasonal -->
<section class="page" style="left:36px">
  <div class="florals" role="img" aria-label="Pink rose and green leaf floral border"></div>
  <div class="sheet"></div>

  <div class="at logo-dot" style="left:48px;top:52px"></div>
  <div class="at brand" style="left:76px;top:58px">MARBRE COQUETTE</div>

  <div class="at address" style="left:200px;top:43px">
    1480 Bayview Rd, Weston,<br>Florida 33327<br>
    <span class="tel"><svg viewBox="0 0 24 24"><path d="M6.6 10.8a15.1 15.1 0 0 0 6.6 6.6l2.2-2.2c.3-.3.7-.4 1-.2 1.1.4 2.3.6 3.6.6.6 0 1 .4 1 1V20c0 .6-.4 1-1 1A17 17 0 0 1 3 4c0-.6.4-1 1-1h3.5c.6 0 1 .4 1 1 0 1.3.2 2.5.6 3.6.1.3 0 .7-.2 1z"/></svg> 954-555-0186</span><br>
    @ Marbrecoquette
  </div>

  <div class="rule" style="left:32px;width:303px;top:113px"></div>
  <div class="at title" style="left:32px;width:303px;top:120px">Seasonal Menu</div>
  <div class="at sub" style="left:32px;width:303px;top:137px">Upon availability</div>
  <div class="rule" style="left:32px;width:303px;top:149px"></div>

  <div class="at h" style="left:32px;top:160px">Soups</div>
  <div class="at" style="left:32px;top:172px;width:136px">
    <div class="row">Lorraine<span class="lead"></span>$6.99</div>
  </div>
  <div class="rule" style="left:32px;width:136px;top:200px"></div>

  <div class="at h" style="left:32px;top:215px">Baba au rhum <span class="tag">CONTAIN ALCOHOL</span></div>
  <div class="at" style="left:32px;top:229px;width:136px">
    <div class="row">Chocolate / Hazella<span class="lead"></span>$7.80</div>
    <div class="row">Vanilla / Orange / Pineapple<span class="lead"></span>$7.80</div>
  </div>

  <div class="vr" style="left:183px;top:157px;height:96px"></div>

  <div class="at h" style="left:200px;top:160px">Travel cakes <span class="mark vg"></span></div>
  <div class="at" style="left:200px;top:172px;width:135px">
    <div class="row">Pistachio raspberry opera<span class="mark"></span><span class="lead"></span>$8.80</div>
    <p class="desc">Pistachio joconde cake layered with pistachio buttercream, chocolate ganache and raspberry gelée.</p>
  </div>
  <div class="at" style="left:200px;top:205px;width:135px">
    <div class="row">Banana pecan<span class="mark"></span><span class="lead"></span>$6.00</div>
    <div class="row">Banana walnut<span class="mark"></span><span class="lead"></span>$6.00</div>
    <div class="row">Banana chocolate chips<span class="lead"></span>$6.00</div>
    <div class="row">Blueberry<span class="lead"></span>$6.00</div>
  </div>

  <div class="rule" style="left:32px;width:303px;top:262px"></div>
  <div class="at title" style="left:32px;width:303px;top:270px">Vegan Treats</div>
  <div class="rule" style="left:32px;width:303px;top:292px"></div>

  <div class="at" style="left:32px;top:301px;width:136px">
    <div class="row">Florentine<span class="lead"></span>$6.90</div>
    <p class="desc">Chou bun topped with vegan creamy cheese garlic and herbs, sauté spinach, 2 omelettes</p>
  </div>
  <div class="vr" style="left:183px;top:298px;height:44px"></div>
  <div class="at" style="left:200px;top:301px;width:135px">
    <div class="row">Avocado toast<span class="lead"></span>$6.90</div>
    <p class="desc">Chou bun topped with vegan creamy cheese with garlic and herbs, avocado smash, sliced tomatoes, microgreens and sesame seeds served with a side of spicy honey</p>
  </div>

  <div class="rule" style="left:32px;width:303px;top:347px"></div>
  <div class="at h" style="left:32px;width:94px;top:353px;text-align:center">Cookies</div>
  <div class="at h" style="left:126px;width:115px;top:353px;text-align:center">Muffins</div>
  <div class="at h" style="left:241px;width:94px;top:353px;text-align:center">Verrines</div>
  <div class="vr" style="left:126px;top:347px;height:85px"></div>
  <div class="vr" style="left:241px;top:347px;height:85px"></div>
  <div class="rule" style="left:32px;width:303px;top:368px"></div>

  <div class="at tight" style="left:32px;top:380px;width:88px">
    <div class="row">Chocolate chip<span class="lead"></span>$5.20</div>
    <div class="row">Double chocolate chip<span class="lead"></span>$5.20</div>
    <div class="row">Oatmeal cinnamon<span class="lead"></span>$5.20</div>
    <div class="row">Mini cookies (3 pack)<span class="lead"></span>+$2.50</div>
  </div>
  <div class="at tight" style="left:139px;top:380px;width:96px">
    <div class="row">Banana chocolate chip<span class="lead"></span>$5.20</div>
    <div class="row">Chocolate/chocolate chips<span class="lead"></span>$5.20</div>
    <div class="row">Blueberry<span class="lead"></span>$5.20</div>
    <div class="row">Banana walnut<span class="mark"></span><span class="lead"></span>+$2.50</div>
  </div>
  <div class="at tight" style="left:257px;top:380px;width:78px">
    <div class="row">Chocolate cake<span class="mark gf"></span><span class="lead"></span>$5.20</div>
    <div class="row">Lemon berries<span class="mark gf"></span><span class="lead"></span>$5.20</div>
    <div class="row">Coconut cake<span class="mark gf"></span><span class="lead"></span>$5.20</div>
  </div>

  <div class="at legend" style="left:53px;top:443px">
    <span><i style="background:#7a5634"></i>Contains nuts</span>
    <span><i style="background:#e79a9a"></i>Contains almonds</span>
    <span><i style="background:var(--teal)"></i>Contains walnuts</span>
    <span><i style="background:#d2a36b;border-radius:1px"></i>Gluten free</span>
    <span><i style="background:#9ccc7a"></i>Vegan</span>
  </div>
</section>

<!-- Page 2: brunch -->
<section class="page" style="left:417px">
  <div class="florals" role="img" aria-label="Pink rose and green leaf floral border"></div>
  <div class="sheet"></div>

  <div class="at title" style="left:0;width:368px;top:23px">All Day Brunch</div>
  <div class="at sub" style="left:0;width:368px;top:41px">Unique flavors</div>

  <div class="at" style="left:32px;top:64px;width:135px">
    <div class="row">Grilled cheese sandwich<span class="lead"></span>$14.00</div>
    <p class="desc">Big chou bun 2 slices of fontina cheese, ham and bacon* - the ultimate grilled cheese sandwich "à la eclair"</p>
  </div>
  <div class="at" style="left:32px;top:113px;width:135px">
    <div class="row">Croque monsieur<span class="lead"></span>$15.00</div>
    <p class="desc">Big chou bun served hot filled with creamy bechamel sauce, gruyère cheese, ham and bacon*</p>
  </div>
  <div class="at" style="left:32px;top:163px;width:135px">
    <div class="row">Croque madame<span class="lead"></span>$16.50</div>
    <p class="desc">Big chou bun served hot filled with creamy bechamel sauce, gruyère cheese, ham and bacon* and topped with an egg sunny side up</p>
  </div>

  <div class="at sides" style="left:183px;top:58px;width:152px;height:145px"></div>
  <div class="at h" style="left:183px;width:152px;top:68px;text-align:center">Sides</div>
  <div class="rule" style="left:196px;width:126px;top:82px;height:0;border-bottom:0"></div>
  <div class="at" style="left:200px;top:85px;width:116px">
    <div class="row">Eggs(1)<span class="lead" style="border:0"></span>$2.99</div>
    <div class="row">Bacon (4 slices)<span class="lead" style="border:0"></span>$4.00</div>
    <div class="row">Salmon<span class="lead" style="border:0"></span>$3.50</div>
    <div class="row">Pancakes<span class="lead" style="border:0"></span>$3.50</div>
    <div class="row">Avocado smash<span class="lead" style="border:0"></span>$2.50</div>
    <div class="row">Fruit bowl<span class="lead" style="border:0"></span>$5.25</div>
    <div class="row">Green salad<span class="lead" style="border:0"></span>$3.50</div>
  </div>
  <div class="rule" style="left:196px;width:126px;top:178px;height:0;border-bottom:0"></div>
  <p class="at note" style="left:183px;width:152px;top:183px">*Also available<br>Turkey bacon, turkey ham</p>

  <div class="rule" style="left:32px;width:303px;top:220px"></div>
  <div class="at h" style="left:32px;width:151px;top:228px;text-align:center">Eggcellent choices</div>
  <div class="at h" style="left:183px;width:152px;top:228px;text-align:center">Pancakes</div>
  <div class="vr" style="left:183px;top:220px;height:213px"></div>
  <div class="rule" style="left:32px;width:303px;top:245px"></div>
  <div class="at sub" style="left:32px;width:136px;top:252px;text-align:left;letter-spacing:.18em">Also available: gluten free bun</div>

  <div class="at" style="left:32px;top:268px;width:135px">
    <div class="row">Eggs florentine<span class="lead"></span>$16.45</div>
    <p class="desc">Chou bun topped with chive cream cheese, sauté spinach, 2 eggs and pink hollandaise sauce</p>
  </div>
  <div class="at" style="left:32px;top:305px;width:135px">
    <div class="row">Eggs benedict<span class="lead"></span>$16.45</div>
    <p class="desc">Chou bun topped whipped chive cream cheese, ham, 2 eggs, and pink hollandaise sauce</p>
  </div>
  <div class="at" style="left:32px;top:343px;width:135px">
    <div class="row">Avocado &amp; eggs<span class="lead"></span>$17.45</div>
    <p class="desc">Chou bun topped with chunky avocado smash, crumbled feta, 2 eggs, topped with spicy honey, oil, chili flakes and sesame</p>
  </div>
  <div class="at" style="left:32px;top:383px;width:135px">
    <div class="row">Eggs royal<span class="lead"></span>$18.50</div>
    <p class="desc">Chou bun, topped with whipped cream cheese with chives, smoked salmon, diced red onion, 2 eggs, pink hollandaise sauce, sesame seeds</p>
  </div>

  <div class="at" style="left:200px;top:268px;width:135px">
    <div class="row">O.M.G. eggs &amp; bacon<span class="lead"></span>$16.50</div>
    <p class="desc">4 pancakes topped with grated gruyère, bacon, an egg sunny side up and served with a side of maple syrup</p>
  </div>
  <div class="at" style="left:200px;top:305px;width:135px">
    <div class="row">Classic hazella &amp; berries<span class="lead"></span>$16.50</div>
    <p class="desc">4 pancakes topped with Hazella, fresh berries and whipped cream</p>
  </div>
  <div class="at" style="left:200px;top:343px;width:135px">
    <div class="row">Tropical guava &amp; cheese<span class="lead"></span>$16.00</div>
    <p class="desc">4 pancakes topped with guava cream, cream cheese frosting.</p>
  </div>
  <div class="at" style="left:200px;top:383px;width:135px">
    <div class="row">Oriental<span class="mark"></span><span class="lead"></span>$14.50</div>
    <p class="desc">4 pancakes topped with orange cream, caramelized pistachios, crunchy phyllo and drizzled with honey cinnamon syrup</p>
  </div>

  <div class="rule" style="left:32px;width:303px;top:431px"></div>
  <div class="at legend" style="left:53px;top:443px">
    <span><i style="background:#7a5634"></i>Contains nuts</span>
    <span><i style="background:#e79a9a"></i>Contains almonds</span>
    <span><i style="background:var(--teal)"></i>Contains walnuts</span>
    <span><i style="background:#d2a36b;border-radius:1px"></i>Gluten free</span>
    <span><i style="background:#9ccc7a"></i>Vegan</span>
  </div>
</section>

<!-- Page 3: beverages -->
<section class="page" style="left:797px">
  <div class="florals" role="img" aria-label="Pink rose and green leaf floral border"></div>
  <div class="sheet"></div>

  <div class="at title" style="left:0;width:368px;top:23px">Coffess &amp; Beverages</div>
  <div class="rule" style="left:32px;width:303px;top:49px"></div>

  <div class="at h" style="left:32px;top:59px">Mocktails</div>
  <div class="at" style="left:200px;top:55px;width:135px">
    <div class="row">Shirley temple<span class="lead" style="border:0"></span>$6.30</div>
    <p class="desc">Ginger ale and grenadine mocktail garnished with maraschino cherry.</p>
  </div>
  <div class="at" style="left:32px;top:86px;width:135px">
    <div class="row">Mango lychee<span class="lead" style="border:0"></span>$6.50</div>
    <p class="desc">Refreshing mix of lychee and mango</p>
  </div>
  <div class="at" style="left:200px;top:86px;width:135px">
    <div class="row">Pina colada<span class="lead" style="border:0"></span>$6.30</div>
    <p class="desc">A tropical classic mocktail of pineapple and coconut</p>
  </div>

  <div class="rule" style="left:32px;width:303px;top:118px"></div>
  <div class="at h" style="left:32px;top:130px">Iced coffee</div>
  <div class="at" style="left:32px;top:144px;width:78px">
    <div class="row">Iced espresso<span class="lead"></span>$4.00</div>
    <div class="row">Iced cappuccino<span class="lead"></span>$4.55</div>
    <div class="row">Iced latte<span class="lead"></span>$4.75</div>
  </div>
  <div class="vr" style="left:127px;top:128px;height:52px"></div>
  <div class="at h" style="left:142px;top:130px">Hot coffee</div>
  <div class="at" style="left:142px;top:144px;width:82px">
    <div class="row">Filter coffee<span class="lead"></span>$2.40</div>
    <div class="row">Espresso<span class="lead"></span>$2.75</div>
    <div class="row">Cappuccino<span class="lead"></span>$3.50</div>
  </div>
  <div class="at" style="left:247px;top:144px;width:88px">
    <div class="row">Latte<span class="lead"></span>$3.70</div>
    <div class="row">Americano<span class="lead"></span>$3.00</div>
    <div class="row">Espresso macchiato<span class="lead"></span>$3.00</div>
  </div>

  <div class="rule" style="left:32px;width:303px;top:191px"></div>
  <div class="at h" style="left:32px;top:204px">Chocolate</div>
  <div class="at" style="left:32px;top:217px;width:135px">
    <div class="row">Chocolate hot<span class="lead" style="border:0"></span>$4.95</div>
    <div class="row">Chocolate cold<span class="lead" style="border:0"></span>$4.95</div>
    <div class="row">Whipped cream<span class="lead" style="border:0"></span>+$1.00</div>
  </div>
  <div class="vr" style="left:183px;top:200px;height:54px"></div>
  <div class="at h" style="left:200px;top:204px">Matcha</div>
  <div class="at" style="left:200px;top:217px;width:135px">
    <div class="row">Matcha tea<span class="lead" style="border:0"></span>$3.20</div>
    <div class="row">Matcha latte hot<span class="lead" style="border:0"></span>$3.95</div>
    <div class="row">Matcha latte cold<span class="lead" style="border:0"></span>$3.95</div>
  </div>

  <div class="rule" style="left:32px;width:303px;top:263px"></div>
  <div class="at h" style="left:32px;top:276px">Cold drinks</div>
  <div class="at" style="left:32px;top:289px;width:135px">
    <div class="row">Isla spring water 16 oz<span class="lead" style="border:0"></span>$3.70</div>
    <div class="row">San Velino<span class="lead" style="border:0"></span>$4.70</div>
    <div class="row">Cola classic / diet<span class="lead" style="border:0"></span>$4.75</div>
    <div class="row">Perla sparkling<span class="lead" style="border:0"></span>$4.00</div>
    <div class="row">Homemade lemonade<span class="lead" style="border:0"></span>$6.50</div>
    <div class="row">Mint lemonade<span class="lead" style="border:0"></span>$6.50</div>
    <div class="row">Strawberry lemonade<span class="lead" style="border:0"></span>$6.50</div>
    <div class="row">Lavender lemonade<span class="lead" style="border:0"></span>$6.50</div>
    <div class="row">Orange juice<span class="lead" style="border:0"></span>$4.70</div>
  </div>
  <div class="vr" style="left:183px;top:272px;height:125px"></div>
  <div class="at h" style="left:200px;top:276px">Tea</div>
  <div class="at" style="left:200px;top:289px;width:135px">
    <div class="row">Earl grey<span class="lead" style="border:0"></span>$3.50</div>
    <div class="row">Darjeeling<span class="lead" style="border:0"></span>$3.50</div>
    <div class="row">Giger lemongrass<span class="lead" style="border:0"></span>$3.50</div>
    <div class="row">Camomile<span class="lead" style="border:0"></span>$3.50</div>
    <div class="row">Mint vervain &amp; herbs<span class="lead" style="border:0"></span>$3.50</div>
    <div class="row">Fruit symphony<span class="lead" style="border:0"></span>$3.50</div>
    <div class="row">Dragon sencha green tea<span class="lead" style="border:0"></span>$3.50</div>
    <div class="row">Lavender lemonade<span class="lead" style="border:0"></span>$3.50</div>
    <div class="row">Iced tea<span class="lead" style="border:0"></span>$3.50</div>
  </div>

  <div class="at h" style="left:0;width:368px;top:422px;text-align:center">Syrups - Sauces - Toppings</div>
  <p class="at extras" style="left:0;width:368px;top:437px">
    Vanilla | Hazelnut | Caramel | Mocha | Lavender | Almond (ask for our sugar free options) + $1.00<br>
    Dark or white chocolate sauce + $1.00 extra shot + $1.00 decaf + $1.00
  </p>
</section>

</body>
</html>
```